Business cards and stationary for Mortgage Company
Brightwell Lending Partners Inc.
Professional
Peter K Ostrand
Licensed Mortgage Originator
47 Alder Brook Lane
Newtown, Pa 18977
1-855-314-HOME (4663)
peterkostrand@brightwelllendingpartners.example
www.brightwelllendingpartners.example
NMLS# 417205 and NMLS #418362
Looking for stationary and business cards to use logo with black letters on white background, and examples using white letters on black ground . Red graphic is the same on either choice.
Just the logo in either black on white, or white on black background.

```html
<!DOCTYPE html>
<html lang="en">
<head>
<meta charset="utf-8">
<title>Brightwell Lending Partners Inc. — Stationery</title>
<link rel="stylesheet" href="https://fonts.googleapis.com/css2?family=Libre+Baskerville&family=Open+Sans:wght@400;600&display=swap">
<style>
  :root{
    --bg:#d9d9d7;
    --paper:#ffffff;
    --ink:#1c1c1c;
    --ink-soft:#5a5a5a;
    --black:#141414;
    --red:#d3202c;
    --rule:#e3e3e3;
  }
  *{box-sizing:border-box;margin:0;padding:0}
  html,body{width:1200px;height:840px;overflow:hidden;background:var(--bg)}
  body{position:relative;font-family:"Open Sans",Arial,sans-serif;color:var(--ink)}

  .sheet{position:absolute;background:var(--paper);box-shadow:0 2px 10px rgba(0,0,0,.18)}
  .brand{font-family:"Libre Baskerville",Georgia,serif;color:var(--ink);white-space:nowrap;display:flex;align-items:center;gap:8px}
  .brand .mark{width:10px;height:10px;background:var(--red);flex:none}
  .brand--light{color:#fff}

  /* Letterhead */
  .letterhead{left:40px;top:40px;width:540px;height:760px;padding:48px 56px 0}
  .letterhead .brand{justify-content:center;font-size:22px}
  .letterhead .rule{height:1px;background:var(--rule);margin:22px 0 40px}
  .letter-body{font-size:12px;line-height:1.75;color:var(--ink-soft)}
  .letter-body p{margin-bottom:16px}
  .signature{width:150px;height:46px;margin:6px 0 8px;background:linear-gradient(90deg,#eee,#f7f7f7)}
  .signer{font-size:12px;color:var(--ink)}
  .letter-footer{position:absolute;left:0;right:0;bottom:0}
  .letter-footer .contacts{display:flex;flex-wrap:wrap;justify-content:center;gap:4px 18px;padding:0 30px 14px;font-size:10px;color:var(--ink-soft)}
  .letter-footer .band{height:14px;background:var(--red)}

  /* Envelope */
  .envelope-back{left:630px;top:40px;width:530px;height:170px;background:var(--black);padding:22px 26px}
  .envelope-back .web{display:flex;align-items:center;gap:8px;color:#ddd;font-size:11px}
  .envelope-back .web span{width:8px;height:8px;background:var(--red)}
  .envelope-front{left:630px;top:230px;width:530px;height:250px;padding:28px 30px}
  .envelope-front .brand{font-size:17px}
  .return-address{margin-top:10px;font-size:10.5px;color:var(--ink-soft);line-height:1.6}
  .envelope-front .band{position:absolute;left:0;right:0;bottom:0;height:10px;background:var(--red)}

  /* Business cards */
  .card{width:255px;height:300px}
  .card-front{left:630px;top:500px;padding:26px 22px}
  .card-front .brand{font-size:15px;gap:6px}
  .card-front .rule{height:1px;background:var(--rule);margin:16px 0}
  .card-name{font-size:14px;font-weight:600}
  .card-title{font-size:10px;color:var(--red);margin:2px 0 12px}
  .card-details{font-size:9.5px;line-height:1.7;color:var(--ink-soft)}
  .card-front .band{position:absolute;left:0;right:0;bottom:0;height:8px;background:var(--red)}
  .card-back{left:905px;top:500px;background:var(--black);display:flex;align-items:center;justify-content:center}
  .card-back .brand{font-size:15px;gap:6px}
  .card-back .band{position:absolute;left:0;right:0;bottom:0;height:8px;background:var(--red)}
</style>
</head>
<body>

<section class="sheet letterhead">
  <div class="brand">Brightwell Lending Partners<span class="mark"></span></div>
  <div class="rule"></div>
  <div class="letter-body">
    <p>Hello,</p>
    <p>Thank you for considering us for your home financing needs. Our team reviews every application with care and explains each step so you always know where your loan stands.</p>
    <p>We look forward to working with you and helping you reach the closing table with confidence.</p>
    <p>Sincerely,</p>
  </div>
  <div class="signature" role="img" aria-label="Handwritten signature"></div>
  <div class="signer">Peter K Ostrand</div>
  <footer class="letter-footer">
    <div class="contacts">
      <span>47 Alder Brook Lane, Newtown, Pa 18977</span>
      <span>1-855-314-HOME (4663)</span>
      <span>peterkostrand@brightwelllendingpartners.example</span>
      <span>www.brightwelllendingpartners.example</span>
    </div>
    <div class="band"></div>
  </footer>
</section>

<section class="sheet envelope-back">
  <div class="web"><span></span>www.brightwelllendingpartners.example</div>
</section>

<section class="sheet envelope-front">
  <div class="brand">Brightwell Lending Partners<span class="mark"></span></div>
  <div class="return-address">47 Alder Brook Lane<br>Newtown, Pa 18977</div>
  <div class="band"></div>
</section>

<section class="sheet card card-front">
  <div class="brand">Brightwell Lending Partners<span class="mark"></span></div>
  <div class="rule"></div>
  <div class="card-name">Peter K Ostrand</div>
  <div class="card-title">Licensed Mortgage Originator</div>
  <div class="card-details">
    NMLS# 417205 &nbsp;|&nbsp; NMLS #418362<br>
    1-855-314-HOME (4663)<br>
    peterkostrand@brightwelllendingpartners.example<br>
    www.brightwelllendingpartners.example<br>
    47 Alder Brook Lane<br>
    Newtown, Pa 18977
  </div>
  <div class="band"></div>
</section>

<section class="sheet card card-back">
  <div class="brand brand--light">Brightwell Lending Partners<span class="mark"></span></div>
  <div class="band"></div>
</section>

</body>
</html>
```